One of Australia's fastest growing Financial Company looking for an updated business card design!

Meridale Holdings Australia is looking for an updated design for our business cards. We would like to keep up our professional appearances and have get new exciting design that fits our company.

The Meridale aim is to facilitate and assist clients in every financial requirement that may arise in financial areas.

We would to see the design to use colour blue and we like the clouds in the background. We have attached two designs we have use before but we need something with more professional and easy to read design.

We would like the website in the back of the card; the employees name more central and stands out; only a postal address; a list of all our locations along the bottom (Sydney, Melbourne, Brisbane, Singapore)

Looking forward to seeing the designs come in!

Target Market(s)

Other Industry Professionals
Middle Class Families

Industry/Entity Type

Finance

Contact Information for Business Card

Name; Company Role; Office Number; Mobile Number; Email Address; Website; Postal Address; Locations

Font styles to use
Serif
Sans Serif

Colors
0492cd
33a6d7
85cae6
85acd3
3176b5
0455a3
cee9f5
d5e2ee

Requirements
Must have
• Name; Company Role; Office Number; Mobile Number; Email Address; Website; Postal Address; Locations
Nice to have
• The colour blue, clouds on the background

```html
<!DOCTYPE html>
<html lang="en">
<head>
<meta charset="utf-8">
<title>Meridale Holdings Australia – Business Card Design One</title>
<link rel="stylesheet" href="https://fonts.googleapis.com/css2?family=Source+Sans+3:wght@400;700&display=swap">
<style>
  :root {
    --board: #e3e4e6;
    --title-grey: #6d6e70;
    --sky-deep: #3176b5;
    --sky-mid: #4f86c6;
    --sky-light: #85acd3;
    --cloud: #cee9f5;
    --swoosh-edge: #0455a3;
    --brand-blue: #0492cd;
    --name-blue: #2f6db3;
    --role-red: #e2412c;
    --paper: #ffffff;
    --soft-text: #d5e2ee;
    --rule: #a9c4e2;
  }
  html, body {
    margin: 0;
    width: 1200px;
    height: 1200px;
    overflow: hidden;
    background: var(--board);
    font-family: "Source Sans 3", sans-serif;
  }
  .board { position: relative; width: 1200px; height: 1200px; }
  .board-title {
    position: absolute; left: 110px; top: 68px; margin: 0;
    font-size: 29px; font-weight: 700; color: var(--title-grey);
    letter-spacing: 0.2px;
  }
  .card {
    position: absolute; width: 644px; height: 358px;
    border-radius: 24px; overflow: hidden;
  }
  .card--front { left: 104px; top: 212px; }
  .card--back { left: 445px; top: 639px; }
  .card svg { display: block; }
  .sky-fill { fill: url(#sky); }
  .swoosh-edge { fill: var(--swoosh-edge); }
  .swoosh { fill: var(--paper); }
  .brand-name { font-size: 58px; font-weight: 400; fill: var(--brand-blue); }
  .holder-name { font-size: 30px; fill: var(--name-blue); }
  .holder-role { font-size: 16px; fill: var(--role-red); }
  .company { font-size: 18px; font-weight: 700; fill: var(--paper); }
  .contact { font-size: 14px; fill: var(--paper); }
  .locations { font-size: 19px; fill: var(--soft-text); }
  .rule { stroke: var(--rule); stroke-width: 1; }
  .about { font-size: 14.4px; fill: var(--paper); }
  .website { font-size: 24px; fill: var(--paper); letter-spacing: 0.3px; }
</style>
</head>
<body>
<main class="board">
  <h1 class="board-title">BUISNESS CARD DESIGN ONE</h1>

  <svg width="0" height="0" style="position:absolute">
    <defs>
      <linearGradient id="sky" x1="0" y1="0" x2="1" y2="1">
        <stop offset="0" stop-color="#6f9bd0"/>
        <stop offset="0.5" stop-color="#4f86c6"/>
        <stop offset="1" stop-color="#3f7cc0"/>
      </linearGradient>
      <radialGradient id="cloud-glow" cx="0.5" cy="0.5" r="0.5">
        <stop offset="0" stop-color="#ffffff" stop-opacity="0.85"/>
        <stop offset="1" stop-color="#ffffff" stop-opacity="0"/>
      </radialGradient>
    </defs>
  </svg>

  <section class="card card--front">
    <svg width="644" height="358" viewBox="0 0 644 358">
      <g role="img" aria-label="Blue sky with soft white clouds">
        <rect class="sky-fill" width="644" height="358"/>
        <ellipse cx="200" cy="150" rx="260" ry="60" fill="url(#cloud-glow)"/>
      </g>
      <path class="swoosh-edge" d="M368 0 C320 12 300 52 330 78 C400 138 540 152 644 158 L644 0 Z"/>
      <path class="swoosh" d="M368 0 C318 10 298 50 328 74 C398 126 540 140 644 146 L644 0 Z"/>
      <text class="holder-name" x="390" y="56">Claire Hollis</text>
      <text class="holder-role" x="390" y="78">Investment Consultant</text>
      <text class="brand-name" x="38" y="168">Meridale</text>
      <text class="company" x="327" y="218">Meridale Holdings Australia Pty Ltd</text>
      <text class="contact" x="327" y="239">Off No: (02) 5190 2718  Mobile No: 0412 386 954</text>
      <text class="contact" x="327" y="259">Email : info@meridaleholdings.com.au</text>
      <text class="contact" x="327" y="278">Harbourview Post Shop PO BOX 3187</text>
      <line class="rule" x1="322" y1="290" x2="601" y2="290"/>
      <text class="locations" x="322" y="312">Sydney, Melbourne,</text>
      <text class="locations" x="322" y="330">Brisbane, Singapore</text>
      <line class="rule" x1="322" y1="342" x2="601" y2="342"/>
    </svg>
  </section>

  <section class="card card--back">
    <svg width="644" height="358" viewBox="0 0 644 358">
      <g role="img" aria-label="Blue sky with soft white clouds">
        <rect class="sky-fill" width="644" height="358"/>
        <ellipse cx="420" cy="140" rx="200" ry="90" fill="url(#cloud-glow)" opacity="0.5"/>
      </g>
      <path class="swoosh-edge" d="M0 0 L336 0 C348 32 322 76 270 104 C200 140 90 154 0 158 Z"/>
      <path class="swoosh" d="M0 0 L336 0 C345 30 320 70 270 95 C200 128 90 140 0 144 Z"/>
      <text class="brand-name" x="34" y="77">Meridale</text>
      <text class="about" x="30" y="191">
        <tspan x="30">Meridale Holdings Australia Pty Ltd was formed as a rebuttal to faceless</tspan>
        <tspan x="30" dy="19.2">financial institutions that treat people as a commodity. We believe in</tspan>
        <tspan x="30" dy="19.2">personal service and giving value to our clients. We're specialists in</tspan>
        <tspan x="30" dy="19.2">helping people reduce debt and increase wealth. Contact us now</tspan>
        <tspan x="30" dy="19.2">and we'll tell you how we can do that for you.</tspan>
      </text>
      <text class="website" x="34" y="317">www.meridaleholdings.com.au</text>
    </svg>
  </section>
</main>
</body>
</html>
```